Land Buying Company Needs Letterhead for Direct Mail Marketing to Land Owners

We are looking for a professional letterhead that we will be including in our direct mail marketing. We will be sending this to land owners who may be interested in selling or purchasing land.

The letterhead needs to be editable. Headers and footers would look nice, but we are open. We would want it to include our address, website, phone, and email info. For right now the address to use for design purposes would the following:

Address: 415 Bramwell Avenue #600
Dallas, TX 75219
Website - www.quillridgeacres.example
Email - info@quillridgeacres.example
Phone - 866-402-ACRE

I have attached our logo zip file that we just had done on Pixel Guild. Let me know what questions you have, and thank you.

```html
<!DOCTYPE html>
<html lang="en">
<head>
<meta charset="utf-8">
<title>Quillridge Acres Letterhead</title>
<link href="https://fonts.googleapis.com/css2?family=Montserrat:wght@400;600;700&display=swap" rel="stylesheet">
<style>
  :root {
    --backdrop: #d6d6d6;
    --paper: #ffffff;
    --forest: #3e5c17;
    --leaf: #8dc63f;
    --ink: #1a1a1a;
    --watermark: #f0f1ef;
  }
  * { box-sizing: border-box; margin: 0; padding: 0; }
  html, body { width: 1200px; height: 898px; overflow: hidden; }
  body {
    background: var(--backdrop);
    font-family: "Montserrat", Arial, sans-serif;
    position: relative;
  }
  .letterhead {
    position: absolute;
    left: 296px; top: 19px;
    width: 608px; height: 860px;
    background: var(--paper);
    box-shadow: 0 6px 24px rgba(0,0,0,.18);
  }
  .brand {
    position: absolute; top: 42px; left: 0; right: 0;
    display: flex; align-items: center; justify-content: center; gap: 16px;
  }
  .brand-disc {
    width: 58px; height: 58px; border-radius: 50%;
    background: var(--forest);
  }
  .brand-name {
    font-weight: 700; font-size: 30px; letter-spacing: 2px;
    color: var(--forest); line-height: 1;
  }
  .contact-band {
    position: absolute; top: 122px; left: 40px; right: 40px;
    border-top: 1.5px solid var(--forest);
    border-bottom: 1.5px solid var(--forest);
    height: 26px;
    display: flex; align-items: center; justify-content: space-between;
    padding: 0 4px;
    font-size: 10px; color: var(--ink);
  }
  .contact-item { display: flex; align-items: center; gap: 5px; }
  .contact-icon { width: 10px; height: 10px; fill: var(--leaf); }
  .watermark {
    position: absolute; left: 204px; top: 330px;
    width: 200px; height: 200px; border-radius: 50%;
    background: var(--watermark);
  }
  .footer-rule {
    position: absolute; left: 40px; right: 40px; top: 762px;
    border-top: 1.5px solid var(--forest);
  }
  .footer-address {
    position: absolute; left: 0; right: 0; top: 778px;
    text-align: center; font-size: 10px; line-height: 1.45; color: var(--ink);
  }
  .footer-address strong { font-weight: 700; }
</style>
</head>
<body>
  <main class="letterhead">
    <header class="brand">
      <div class="brand-disc"></div>
      <div class="brand-name">QUILLRIDGE ACRES</div>
    </header>

    <div class="contact-band">
      <span class="contact-item">
        <svg class="contact-icon" viewBox="0 0 10 10"><circle cx="5" cy="5" r="4.5" fill="none" stroke="var(--leaf)" stroke-width="1"/><ellipse cx="5" cy="5" rx="2" ry="4.5" fill="none" stroke="var(--leaf)" stroke-width="1"/><line x1="0.5" y1="5" x2="9.5" y2="5" stroke="var(--leaf)" stroke-width="1"/></svg>
        www.quillridgeacres.example
      </span>
      <span class="contact-item">
        <svg class="contact-icon" viewBox="0 0 10 10"><path d="M2 0.5l1.8 2-1 1.2c.6 1.4 1.6 2.4 3 3l1.2-1 2 1.8-1 1.8C4.5 9 1 5.5.5 1.5z"/></svg>
        866-402-ACRE
      </span>
      <span class="contact-item">
        <svg class="contact-icon" viewBox="0 0 10 10"><rect x="0.5" y="1.5" width="9" height="7" rx="1"/><path d="M1 2.2l4 3 4-3" fill="none" stroke="#fff" stroke-width="0.9"/></svg>
        info@quillridgeacres.example
      </span>
    </div>

    <div class="watermark"></div>

    <div class="footer-rule"></div>
    <footer class="footer-address">
      <strong>Address</strong> - 415 Bramwell Avenue #600<br>
      Dallas, TX 75219
    </footer>
  </main>
</body>
</html>
```